Postcard Design Project A Healthy reminder

Dr.'s Desmond and Lena torvik. Internal Medicine/Family practice. This postcard will be for our patients that we have not seen in a while. Also we need another postcard (the one your designing) with a different heading for New patient's. Do you offer a price break for that? The only thing we would need to change is the heading. Please let me know. Thank you so much! Also can you use the map on the last postcard and our logo I made? I cant find it. Please feel free to call me or email me.

```html
<!DOCTYPE html>
<html lang="en">
<head>
<meta charset="utf-8">
<title>Healthy Reminder Postcard</title>
<link rel="stylesheet" href="https://fonts.googleapis.com/css2?family=Oswald:wght@500;600&family=Roboto+Condensed:wght@400&family=Open+Sans:ital,wght@1,300;1,400&family=Roboto:wght@400;500&display=swap">
<style>
:root{
  --stage:#e6e6e6;
  --paper:#f6f6f4;
  --maroon:#8b1a1a;
  --crimson:#c62828;
  --ink:#2a2a2a;
  --white:#ffffff;
}
*{margin:0;padding:0;box-sizing:border-box}
html,body{width:1200px;height:1001px;overflow:hidden;background:var(--stage)}
.canvas{position:relative;width:1200px;height:1001px}
.card{position:absolute;width:638px;height:425px;background:var(--paper);overflow:hidden}
.card-front{left:120px;top:58px}
.card-back{left:442px;top:518px}
.card svg.shapes{position:absolute;left:0;top:0}
.abs{position:absolute}
.brand-name{font-family:"Roboto",sans-serif;font-weight:500;font-size:13px;color:var(--ink);letter-spacing:.2px;white-space:nowrap}
.brand-tag{font-family:"Roboto",sans-serif;font-weight:500;font-size:7px;letter-spacing:1.6px;color:var(--ink);white-space:nowrap}
.front-brand{left:390px;top:70px;width:240px;text-align:center}
.front-brand .brand-tag{margin-top:52px}
.headline{left:300px;top:190px;width:320px;text-align:center;font-family:"Oswald",sans-serif;font-weight:600;font-size:20px;line-height:29px;color:var(--maroon)}
.tagline{left:440px;top:346px;width:200px;text-align:center;font-family:"Open Sans",sans-serif;font-style:italic;font-weight:300;font-size:20px;line-height:28px;color:var(--white)}
.contact{font-family:"Roboto Condensed",sans-serif;font-size:13.5px;color:var(--white);display:flex;align-items:center;gap:5px;white-space:nowrap}
.contact svg{flex:none}
.contact-phone{left:28px;top:375px}
.contact-web{left:147px;top:375px}
.contact-address{left:28px;top:397px}
.map-band{left:0;top:0;width:638px;height:216px;background:var(--maroon)}
.map{left:17px;top:18px;width:602px;height:158px;background:linear-gradient(90deg,#efe9dc 0%,#ece6d6 55%,#cfe0c0 68%,#bcd5ab 100%)}
.map-caption{left:0;top:184px;width:638px;text-align:center;font-family:"Roboto Condensed",sans-serif;font-size:14px;color:var(--white)}
.back-brand{left:20px;top:264px;width:200px;text-align:center}
.back-brand .brand-tag{margin-top:33px;font-size:6px;letter-spacing:1.4px}
.back-brand .brand-name{font-size:12px}
.visit{left:52px;top:355px;font-family:"Roboto Condensed",sans-serif;font-size:14.5px;color:var(--ink);display:flex;align-items:center;gap:8px}
.social-dot{width:15px;height:15px;border-radius:50%;background:var(--maroon)}
.back-web{left:0;top:377px;width:240px;text-align:center;font-family:"Roboto Condensed",sans-serif;font-size:14.5px;color:var(--maroon)}
.photo-cutout{left:190px;top:208px;width:136px;height:217px;background:linear-gradient(180deg,#ececea 0%,#d9d9d6 60%,#bdbdba 100%);border-radius:40px 40px 6px 6px}
.stamp-box{left:542px;top:236px;width:57px;height:56px;border:1px solid #8a8a8a}
</style>
</head>
<body>
<div class="canvas">

  <section class="card card-front">
    <svg class="shapes" width="638" height="425" viewBox="0 0 638 425">
      <defs>
        <linearGradient id="photoTone" x1="0" y1="0" x2="1" y2="1">
          <stop offset="0" stop-color="#c9b7a0"/>
          <stop offset=".5" stop-color="#e4ddd2"/>
          <stop offset="1" stop-color="#a89a8a"/>
        </linearGradient>
        <linearGradient id="redSweep" x1="0" y1="1" x2="1" y2="0">
          <stop offset="0" stop-color="#8b1a1a"/>
          <stop offset="1" stop-color="#c62828"/>
        </linearGradient>
        <linearGradient id="greySweep" x1="0" y1="1" x2="1" y2="0">
          <stop offset="0" stop-color="#b5b5b5"/>
          <stop offset=".6" stop-color="#3a3a3a"/>
          <stop offset="1" stop-color="#111"/>
        </linearGradient>
      </defs>
      <path role="img" aria-label="Photo of two doctors reviewing a chart in a clinic hallway" d="M0 0 H348 C310 100 296 250 318 364 H0 Z" fill="url(#photoTone)"/>
      <path d="M348 0 H360 C322 110 304 250 350 364 H318 C296 250 310 100 348 0 Z" fill="url(#redSweep)"/>
      <rect x="0" y="364" width="400" height="61" fill="var(--maroon)"/>
      <path d="M368 425 C420 330 520 296 638 300 V309 C530 306 440 335 392 425 Z" fill="url(#greySweep)"/>
      <path d="M392 425 C440 340 530 312 638 312 V425 Z" fill="url(#redSweep)"/>
    </svg>

    <div class="abs front-brand">
      <div class="brand-name">Desmond T Torvik, M.D.</div>
      <div class="brand-tag">A Primary Care Office</div>
    </div>

    <h1 class="abs headline">A Healthy Reminder, It is time<br>for your annual examination.</h1>

    <p class="abs tagline">Your Health is<br>Our Top Priority</p>

    <div class="abs contact contact-phone">
      <svg width="14" height="14" viewBox="0 0 14 14"><circle cx="7" cy="7" r="6.2" fill="none" stroke="#fff" stroke-width="1"/><path d="M4.6 4.2c.4-.4.8-.3 1 .1l.5.9c.1.3 0 .5-.2.7l-.3.3c.4.9 1 1.5 1.9 1.9l.3-.3c.2-.2.4-.3.7-.2l.9.5c.4.2.5.6.1 1-.6.6-1.4.7-2.2.3C6 8.9 5.1 8 4.6 6.9c-.4-.8-.3-1.9 0-2.7z" fill="#fff"/></svg>
      <span>(555) 014-2287</span>
    </div>
    <div class="abs contact contact-web">
      <svg width="14" height="14" viewBox="0 0 14 14"><circle cx="7" cy="7" r="6.2" fill="none" stroke="#fff" stroke-width="1"/><circle cx="7" cy="7" r="3.6" fill="none" stroke="#fff" stroke-width=".9"/><path d="M3.4 7h7.2M7 3.4v7.2" stroke="#fff" stroke-width=".9"/></svg>
      <span>www.torvikmd.com</span>
    </div>
    <div class="abs contact contact-address">
      <svg width="14" height="14" viewBox="0 0 14 14"><circle cx="7" cy="7" r="6.2" fill="none" stroke="#fff" stroke-width="1"/><path d="M7 3.3a2.4 2.4 0 0 0-2.4 2.4c0 1.8 2.4 4.6 2.4 4.6s2.4-2.8 2.4-4.6A2.4 2.4 0 0 0 7 3.3z" fill="#fff"/><circle cx="7" cy="5.7" r=".9" fill="var(--maroon)"/></svg>
      <span>4120 N. Alder Street Suite 210 Fresno, CA 93720</span>
    </div>
  </section>

  <section class="card card-back">
    <div class="abs map-band"></div>
    <div class="abs map" role="img" aria-label="Road map of the Fresno region with a pin marking the office location"></div>
    <p class="abs map-caption">Located at: South East Corner of Alder and Birch</p>

    <div class="abs back-brand">
      <div class="brand-name">Desmond T Torvik, M.D.</div>
      <div class="brand-tag">A Primary Care Office</div>
    </div>

    <div class="abs photo-cutout" role="img" aria-label="Cut-out photo of two doctors in white coats reading a chart"></div>

    <div class="abs visit"><span>Visit us on:</span><span class="social-dot"></span></div>
    <p class="abs back-web">www.torvikmd.com</p>

    <div class="abs stamp-box"></div>
  </section>

</div>
</body>
</html>
```